Velmora Water Purification

We need a website set up on a "Free account" WordPress platform. (This is the type of Wordpress site that you can sign up for and create online for free (not a server-hosted type.)
The website will be for a water purification company. They install devices in homes to purify the water for safer drinking, bathing, and cleaning.
Our logo is attached. Please keep color scheme of the website consistent with the logo.
Water Purification

```html
<!DOCTYPE html>
<html lang="en">
<head>
<meta charset="utf-8">
<title>Velmora Water Purification</title>
<link rel="stylesheet" href="https://fonts.googleapis.com/css2?family=Open+Sans:wght@400;600;700&family=Playfair+Display:ital,wght@1,700&family=Roboto+Condensed:wght@400;700&display=swap">
<style>
:root{
  --navy:#1c2a6e;
  --navy-deep:#141d52;
  --footer:#1b2562;
  --blue:#1e8fd0;
  --blue-dark:#0c5c9c;
  --sky:#3fb0e6;
  --text:#6a6f7a;
  --white:#ffffff;
  --pale:#eef6fb;
}
*{margin:0;padding:0;box-sizing:border-box}
html,body{width:1200px;height:3520px;overflow:hidden}
body{position:relative;background:var(--white);font-family:"Open Sans",sans-serif;color:var(--text)}
.abs{position:absolute}
.script{font-family:"Playfair Display",serif;font-style:italic;font-weight:700}
.btn{position:absolute;display:flex;align-items:center;justify-content:center;background:var(--blue);color:var(--white);font-weight:600;font-size:17px;letter-spacing:1px;border-radius:26px}
.btn.inline{position:static;margin:0 auto}

/* header */
.site-header{left:0;top:0;width:1200px;height:112px;background:var(--white)}
.nav{top:48px;display:flex;gap:40px;font-size:15px;font-weight:600;color:var(--navy);letter-spacing:.5px}
.nav .active{color:var(--blue)}
.brand{left:480px;top:14px;width:240px;height:86px;display:flex;align-items:center;justify-content:center;gap:12px;color:var(--navy);font-weight:700;font-size:30px}
.brand i{width:26px;height:26px;border-radius:50%;background:var(--blue);display:block}

/* hero */
.hero{left:0;top:112px;width:1200px;height:568px;background:linear-gradient(100deg,#dfe6ec 0%,#f4f7f9 40%,#e9eef2 70%,#cfd9e1 100%)}
.hero-circle{left:28px;top:258px;width:360px;height:360px;border-radius:50%;background:radial-gradient(circle,#1e3a86 0%,#162a6a 100%);border:8px solid rgba(255,255,255,.35);color:var(--white);text-align:center;padding:96px 52px 0}
.hero-circle h1{font-size:44px;margin-bottom:28px}
.hero-circle p{font-size:17px;line-height:1.55}
.arrow{width:44px;height:44px;border-radius:50%;top:366px}

/* call band */
.call-band{left:0;top:680px;width:1200px;height:180px;background:linear-gradient(180deg,var(--sky) 0%,var(--blue) 55%,var(--blue-dark) 100%);text-align:center;color:var(--white)}
.call-band p{margin-top:42px;font-size:24px;font-weight:600}
.call-band .phone{font-family:"Roboto Condensed",sans-serif;font-size:68px;letter-spacing:6px;margin-top:6px;font-weight:400}

/* welcome */
.welcome-photo{left:0;top:900px;width:368px;height:440px;background:linear-gradient(160deg,#cdd3d9,#9aa4ae 60%,#3b3f46)}
.welcome h2{left:388px;top:944px;font-size:42px;color:var(--navy)}
.welcome .kicker{left:390px;top:1004px;font-size:14px;color:var(--blue);font-weight:600;letter-spacing:1px}
.welcome .body{left:388px;top:1040px;width:772px;font-size:15px;line-height:1.75}

/* services */
.services{left:0;top:1368px;width:1200px;height:732px;background:linear-gradient(110deg,#5a5249 0%,#8d857b 30%,#c9c6c0 55%,#eef0f2 75%,#f6f8f9 100%)}
.services-circle{left:100px;top:1480px;width:480px;height:480px;border-radius:50%;background:radial-gradient(circle,#1f3c88 0%,#172c6c 100%);border:10px solid rgba(255,255,255,.3);text-align:center;color:var(--white);padding:78px 66px 0;display:flex;flex-direction:column;align-items:center}
.services-circle h2{font-size:46px;margin-bottom:12px}
.services-circle h3{font-size:20px;font-weight:600;line-height:1.4;margin-bottom:12px}
.services-circle p{font-size:14px;line-height:1.65;color:#cfd8ee;margin-bottom:20px}

/* testimonials */
.testimonials{left:0;top:2100px;width:1200px;height:480px;background:linear-gradient(180deg,#ffffff 0%,var(--pale) 100%)}
.section-title{width:1200px;text-align:center;font-size:40px;color:var(--navy)}
.quote-box{left:180px;top:2240px;width:840px;height:230px;background:var(--white);box-shadow:0 4px 18px rgba(30,60,120,.15);padding:28px 48px 0 90px;font-size:15px;line-height:1.7}
.quote-mark{left:200px;top:2262px;font-family:"Playfair Display",serif;font-size:80px;line-height:1;color:var(--blue)}
.client{left:180px;top:2422px;width:840px;text-align:center;font-size:22px;color:var(--navy)}
.dots{left:540px;top:2520px;display:flex;gap:14px}
.dots span{width:14px;height:14px;border-radius:50%;border:2px solid var(--blue)}
.dots .on{background:var(--blue)}

/* news */
.news-card{top:2740px;width:320px}
.news-photo{width:320px;height:212px;background:linear-gradient(150deg,#d9dfe4,#a7b2bb)}
.news-date{position:absolute;left:0;top:180px;background:var(--blue);color:var(--white);font-size:13px;font-weight:600;padding:9px 16px}
.news-card h4{margin-top:30px;font-size:20px;color:var(--navy);white-space:nowrap}
.news-card p{margin-top:10px;font-size:14px;line-height:1.6}
.news-card a{display:block;margin-top:8px;font-size:15px;color:var(--blue);font-weight:600;text-decoration:underline}

/* footer */
.site-footer{left:0;top:3160px;width:1200px;height:288px;background:var(--footer);color:#c8d0ea}
.f-col h5{font-size:16px;color:var(--sky);font-weight:700;letter-spacing:1px;margin-bottom:14px}
.f-col p,.f-col li{font-size:14px;line-height:1.7}
.f-col ul{list-style:none}
.f-col li::before{content:"›";margin-right:10px;color:var(--sky)}
.f-col .btn.inline{margin:16px 0 0}
.f-brand{left:880px;top:3200px;width:240px;height:120px;border-radius:60px;background:var(--navy-deep);display:flex;align-items:center;justify-content:center;gap:12px;color:var(--white);font-weight:700;font-size:30px}
.f-brand i{width:24px;height:24px;border-radius:50%;background:var(--sky);display:block}
.social{top:3362px;display:flex;gap:18px;left:924px}
.social span{width:38px;height:38px;border-radius:50%;background:var(--blue)}
.bottom-bar{left:0;top:3448px;width:1200px;height:72px;background:var(--navy-deep);color:#aab4d6;font-size:14px;display:flex;align-items:center;justify-content:center}
</style>
</head>
<body>

<header class="abs site-header">
  <nav class="abs nav" style="left:196px"><span class="active">■ HOME</span><span>ABOUT</span><span>SERVICES</span></nav>
  <div class="abs brand"><i></i>Velmora</div>
  <nav class="abs nav" style="left:736px"><span>TESTIMONIALS</span><span>NEWS</span><span>CONTACT</span></nav>
</header>

<section class="abs hero" role="img" aria-label="Woman holding a glass of water beside a countertop water purifier in a bright kitchen"></section>
<div class="abs hero-circle">
  <h1 class="script">Velmora</h1>
  <p>Install Devices In Homes To Purify The Water For Safer Drinking, Bathing, And Cleaning.</p>
</div>
<svg class="abs arrow" style="left:12px" viewBox="0 0 44 44"><circle cx="22" cy="22" r="22" fill="rgba(40,40,50,.55)"/><path d="M25 14l-8 8 8 8" stroke="#fff" stroke-width="3" fill="none"/></svg>
<svg class="abs arrow" style="left:1144px" viewBox="0 0 44 44"><circle cx="22" cy="22" r="22" fill="rgba(40,40,50,.55)"/><path d="M19 14l8 8-8 8" stroke="#fff" stroke-width="3" fill="none"/></svg>

<section class="abs call-band">
  <p>Get Water Purification system Installation in Your Home by giving missed on :</p>
  <div class="phone">123 456 7890</div>
</section>

<section class="welcome">
  <div class="abs welcome-photo" role="img" aria-label="Hand filling a glass from a water dispenser"></div>
  <h2 class="abs script">Welcome To Velmora</h2>
  <div class="abs kicker">WATER PURIFICATION</div>
  <p class="abs body">Lorem Ipsum is simply dummy text of the printing and typesetting industry. Lorem Ipsum has been the industry's standard dummy text ever since the 1500s, when an unknown printer took a galley of type and scrambled it to make a type specimen book. It has survived not only five centuries, but also the leap into electronic typesetting, remaining essentially unchanged. It was popularised in the 1960s with the release of Letraset sheets containing Lorem Ipsum passages, and more recently with desktop publishing software like Aldus PageMaker including versions of Lorem Ipsum.</p>
  <div class="btn" style="left:388px;top:1250px;width:192px;height:52px">LEARN MORE</div>
</section>

<section class="abs services" role="img" aria-label="Family in a living room with a wall-mounted water purifier and glasses of water"></section>
<div class="abs services-circle">
  <h2 class="script">Our Services</h2>
  <h3>Install Devices In Homes To Purify The Water</h3>
  <p>Lorem Ipsum is simply dummy text of the printing and typesetting industry. Lorem Ipsum has been the industry's standard dummy text ever since the 1500s, when an unknown printer.</p>
  <div class="btn inline" style="width:192px;height:52px;flex:none">LEARN MORE</div>
</div>

<section class="abs testimonials">
  <svg class="abs" style="left:0;top:240px" width="1200" height="240" viewBox="0 0 1200 240"><path d="M0 120C200 60 400 200 600 130S1000 40 1200 110V240H0Z" fill="#dbeef8"/><path d="M0 170C250 110 450 230 700 170S1050 110 1200 160V240H0Z" fill="#c6e4f4"/></svg>
</section>
<h2 class="abs section-title script" style="left:0;top:2150px">What Our Client Say About Us</h2>
<div class="abs quote-box">Lorem Ipsum is simply dummy text of the printing and typesetting industry. Lorem Ipsum has been the industry's standard dummy text ever since the 1500s, when an unknown printer took a galley of type and scrambled it to make a type specimen book. It has survived not only five centuries, but also the leap into electronic typesetting, remaining essentially unchanged.</div>
<div class="abs quote-mark">“</div>
<div class="abs client script">— Client Name</div>
<div class="abs dots"><span></span><span></span><span class="on"></span><span></span><span></span></div>

<h2 class="abs section-title script" style="left:0;top:2630px">Latest News</h2>
<article class="abs news-card" style="left:80px">
  <div style="position:relative"><div class="news-photo" role="img" aria-label="Hands under running tap water"></div><div class="news-date">November 02, 2017</div></div>
  <h4 class="script">Lorem Ypsum is simply dummy.</h4>
  <p>Lorem Ipsum is simply dummy text of the printing and typesetting industry. Lorem Ipsum has been the industry's standard dummy text ever.</p>
  <a>Read More »</a>
</article>
<article class="abs news-card" style="left:440px">
  <div style="position:relative"><div class="news-photo" role="img" aria-label="Kitchen faucet pouring water into a sink"></div><div class="news-date">December 02, 2017</div></div>
  <h4 class="script">Lorem Ypsum is simply dummy.</h4>
  <p>Lorem Ipsum is simply dummy text of the printing and typesetting industry. Lorem Ipsum has been the industry's standard dummy text ever.</p>
  <a>Read More »</a>
</article>
<article class="abs news-card" style="left:800px">
  <div style="position:relative"><div class="news-photo" role="img" aria-label="Woman drinking a glass of water in a kitchen"></div><div class="news-date">October 02, 2017</div></div>
  <h4 class="script">Lorem Ypsum is simply dummy.</h4>
  <p>Lorem Ipsum is simply dummy text of the printing and typesetting industry. Lorem Ipsum has been the industry's standard dummy text ever.</p>
  <a>Read More »</a>
</article>

<footer class="abs site-footer"></footer>
<div class="abs f-col" style="left:80px;top:3196px;width:230px">
  <h5>ABOUT US</h5>
  <p>Lorem Ipsum is simply dummy text of the printing and typesetting industry. Lorem Ipsum has been the standard.</p>
  <div class="btn inline" style="width:180px;height:48px">LEARN MORE</div>
</div>
<div class="abs f-col" style="left:352px;top:3196px">
  <h5>SITEMAP</h5>
  <ul><li>Home</li><li>About</li><li>Services</li><li>Testimonials</li><li>News</li><li>Contact</li></ul>
</div>
<div class="abs f-col" style="left:608px;top:3196px;width:240px">
  <h5>CONTACT US</h5>
  <p><b style="color:#fff">Velmora</b><br>20 - Lorem Ipsum is simply dummy text of print &amp; type.</p>
  <p style="margin-top:10px">123 - 456 - 7890</p>
  <p style="margin-top:10px">info@velmora-water.com</p>
</div>
<div class="abs f-brand"><i></i>Velmora</div>
<div class="abs social"><span></span><span></span><span></span></div>
<div class="abs bottom-bar">©Velmora Water Purification - 2017 All Right Reserved</div>

</body>
</html>
```